business card - Helicopter Flight Services, Flight School, etc.

We need a business card design for a new helicopter service.

We offer Helicopter Flight Services, Aerial Filming & Photography, Flight School, and Helicopter Tours. In that order.

Summit Bladecraft, Inc.
Harold Tessendy
SummitBladecraft@Lumenpost.com
303-555-0182

Based at the Coldbrook Airport in Van Nuys, CA. The final design should communicate integrity and safety. Pictures or logos at your discretion.

Card back side - surprise me.

```html
<!DOCTYPE html>
<html lang="en">
<head>
<meta charset="utf-8">
<title>Summit Bladecraft, Inc. — Business Card</title>
<link rel="stylesheet" href="https://fonts.googleapis.com/css2?family=Michroma&family=Source+Sans+3:wght@400;600&display=swap">
<style>
  :root {
    --backdrop-top: #1c1c1c;
    --backdrop-bottom: #050505;
    --card-front: #f3f3f3;
    --card-back: #0a8cf8;
    --brand-blue: #0a8cf8;
    --ink: #1b1b1b;
    --white: #ffffff;
  }
  * { margin: 0; padding: 0; box-sizing: border-box; }
  html, body { width: 1200px; height: 900px; overflow: hidden; }
  body {
    position: relative;
    background: linear-gradient(180deg, var(--backdrop-top), var(--backdrop-bottom));
    font-family: "Source Sans 3", "Myriad Pro", sans-serif;
  }
  .card {
    position: absolute;
    top: 184px;
    height: 490px;
    border-radius: 14px;
    text-align: center;
  }
  .card-front { left: 299px; width: 301px; background: var(--card-front); }
  .card-back { left: 645px; width: 304px; background: var(--card-back); color: var(--white); }

  .brand-mark {
    position: absolute;
    left: 50%;
    top: 52px;
    width: 56px;
    height: 56px;
    margin-left: -28px;
    border-radius: 50%;
    background: var(--brand-blue);
  }
  .brand-name {
    position: absolute;
    left: 0; right: 0;
    top: 136px;
    font-family: "Source Sans 3", sans-serif;
    font-size: 17px;
    font-weight: 600;
    line-height: 21px;
    color: var(--brand-blue);
  }
  .person-name {
    position: absolute;
    left: 0; right: 0;
    top: 343px;
    font-size: 18px;
    font-weight: 600;
    color: var(--brand-blue);
  }
  .contact-list {
    position: absolute;
    left: 0; right: 0;
    top: 398px;
    list-style: none;
    font-size: 14px;
    line-height: 20px;
    color: var(--ink);
  }
  .contact-list li { display: flex; justify-content: center; align-items: center; gap: 5px; }
  .contact-list svg { width: 10px; height: 10px; }
  .icon-phone { fill: var(--brand-blue); }
  .icon-mail rect { fill: var(--brand-blue); }
  .icon-mail path { fill: none; stroke: var(--card-front); stroke-width: 2; }

  .back-title {
    position: absolute;
    left: 0; right: 0;
    top: 254px;
    font-family: "Michroma", sans-serif;
    font-size: 15px;
    font-weight: 400;
    line-height: 20px;
    letter-spacing: 0.5px;
  }
  .service-list {
    position: absolute;
    left: 0; right: 0;
    top: 322px;
    list-style: none;
    font-size: 14px;
    font-weight: 600;
    line-height: 22px;
  }
  .service-list li + li { margin-top: 15px; }
</style>
</head>
<body>
  <section class="card card-front" aria-label="Card front">
    <span class="brand-mark"></span>
    <p class="brand-name">Summit Bladecraft, Inc.</p>
    <p class="person-name">Harold Tessendy</p>
    <ul class="contact-list">
      <li>
        <svg class="icon-phone" viewBox="0 0 24 24" aria-hidden="true"><path d="M6.6 10.8a15 15 0 0 0 6.6 6.6l2.2-2.2a1 1 0 0 1 1-.25 11.4 11.4 0 0 0 3.6.57 1 1 0 0 1 1 1V20a1 1 0 0 1-1 1A17 17 0 0 1 3 4a1 1 0 0 1 1-1h3.5a1 1 0 0 1 1 1c0 1.25.2 2.45.57 3.57a1 1 0 0 1-.25 1z"/></svg>
        303-555-0182
      </li>
      <li>
        <svg class="icon-mail" viewBox="0 0 24 24" aria-hidden="true"><rect x="2" y="5" width="20" height="14"/><path d="M2 5l10 8 10-8"/></svg>
        SummitBladecraft@Lumenpost.com
      </li>
    </ul>
  </section>

  <section class="card card-back" aria-label="Card back">
    <h1 class="back-title">SUMMIT BLADECRAFT<br>INC.</h1>
    <ul class="service-list">
      <li>Helicopter Flight Services</li>
      <li>Aerial Filming &amp; Photography</li>
      <li>Flight School</li>
      <li>Helicopter Tours</li>
    </ul>
  </section>
</body>
</html>
```